Komplette Präsentationsvorlage für Psychologen gewünscht
Zielgruppe
Ich bin Psychologe und trainiere in Seminaren Fach- und Führungskräften zu sozialen Kompetenzen.
Aufgabenstellung
Ich möchte eine PPT Vorlage / Folien-Master die folgende Kriterien erfüllt:
1. Passend zu meinem Corporate Design (Farben, Schriftarten, Logo) / Farbwerte #043D5D und #F15A29; Hintergrund überwiegend reinweiß und vereinzelt #D2D2D2
2. Folienmaster sollte folgendermaßen aufgebaut sein: oben rechts das Signet des Logos (Datei: Logo 546), unten rechts fortlaufende Seitenzahlen mit passendem Trenn-Symbol (*) in einer der beiden o.g. Farbwerte
3. Unten links das vollständige Logo in klein (Datei: Logo_2_346)
4. Vielfältige vorgestaltete Layout-Folien, die diverse Content-Darstellungen erlauben und in der Vorlage einprogrammiert sind (siehe unten)
Generell sollte sich das Gesamt-Design an der Vorlage eines Kunden orientieren, das für mich sehr passt. Ich lade zur Inspiration den betreffenden Folienmaster in den Dateien hoch.
Besonders wichtig ist mir Punkt 4 - in der benannten Inspirationsvorlage kann man diese reichhaltigen Layout-Folien gut einsehen durch Klick auf Einfügen > Neue Folien (das kleine Pfeil-Symbol). Vergleichbare Folien sollten bitte ebenfalls im Design gestaltet und genauso einprogrammiert sein, dass ich sie über Klick auf 'Neue Folien direkt auswählen kann. Der Schwerpunkt kann bei mir auf den Kategorien 'Titel und Inhalte', 'Text und Bild' liegen.
Weiterhin sollten auf den Folien ebenfalls verschiedene Grafiken / Piktogramme verfügbar sein, die einem gleichen Stil folgen (auch hier gefällt mir, der 'Comic/Skizzen' Stil meines Kunden sehr gut) - inhaltlich sollten die Grafiken vor allem soziale Situationen, Business-Themen, Verhandlungen, Speech, usw. betreffen. Gerne darf es auch eine Folie mit diversen Grafiken zur Auswahl als Sammlung geben.
(*) Ebenfalls in der Vorlage meines Kunden wird an diversen Stellen innerhalb der Präsentation ein abgerundeter roter 'Strich' verwendet, welcher auch als Trenn-Symbol für die Seitenzahl verwendet wird. Ich wünsche mir ein ähnlich durchgängig designt..

```html
<!DOCTYPE html>
<html lang="de">
<head>
<meta charset="utf-8">
<title>Präsentationsvorlage – Jonas Wendelin</title>
<link rel="stylesheet" href="https://fonts.googleapis.com/css2?family=Cinzel:wght@400;500&family=Roboto:wght@300;400;500&display=swap">
<style>
:root{
  --navy:#043D5D;
  --orange:#F15A29;
  --panel:#ececec;
  --panel-soft:#f1f1f1;
  --stage:#898989;
  --white:#ffffff;
  --sky:#5ccfd8;
}
*{margin:0;padding:0;box-sizing:border-box}
html,body{width:1200px;height:3397px;overflow:hidden;background:var(--stage)}
.canvas{position:relative;width:1200px;height:3397px}
.slide{position:absolute;left:78px;width:1053px;height:593px;background:var(--white);overflow:hidden;font-family:'Roboto',sans-serif;color:var(--navy)}
.slide--1{top:66px}.slide--2{top:733px}.slide--3{top:1400px}.slide--4{top:2068px}.slide--5{top:2735px;background:var(--navy)}
.abs{position:absolute}
.serif{font-family:'Cinzel',serif}

/* brand name */
.brand{position:absolute;display:flex;align-items:center;gap:12px}
.brand__dot{border-radius:50%;background:var(--orange);flex:none}
.brand__name{font-family:'Cinzel',serif;font-weight:400;color:var(--navy);white-space:nowrap;letter-spacing:.02em}
.brand--footer{left:26px;top:528px}
.brand--footer .brand__dot{width:26px;height:26px}
.brand--footer .brand__name{font-size:24px}
.brand--corner{right:30px;top:58px}
.brand--corner .brand__dot{width:16px;height:16px}
.brand--corner .brand__name{font-size:17px}
.brand--light .brand__name{color:var(--white)}

/* page number */
.page-num{position:absolute;left:968px;top:545px;display:flex;align-items:center;gap:10px;font-family:'Cinzel',serif;font-size:22px;color:var(--navy)}
.page-num::before{content:"";width:16px;height:16px;border-radius:50%;background:var(--orange)}
.page-num--on-orange::before{background:var(--white)}
.page-num--light{color:var(--white)}

/* title bubble */
.bubble{position:absolute;left:0;height:86px;border-radius:0 43px 43px 0;padding:18px 0 0 62px;color:var(--white)}
.bubble::after{content:"";position:absolute;left:58px;bottom:-14px;border-left:14px solid transparent;border-right:14px solid transparent;border-top:15px solid inherit}
.bubble--navy{background:var(--navy)}.bubble--navy::after{border-top-color:var(--navy)}
.bubble--orange{background:var(--orange)}.bubble--orange::after{border-top-color:var(--orange)}
.bubble__title{font-family:'Cinzel',serif;font-size:24px;letter-spacing:.02em;line-height:1.2}
.bubble__sub{font-family:'Cinzel',serif;font-size:15px;letter-spacing:.03em}

.tri{display:inline-block;width:0;height:0;border-top:7px solid transparent;border-bottom:7px solid transparent;border-left:10px solid var(--orange)}
.art{position:absolute}

/* slide 1 */
.title-panel{left:41px;top:36px;width:970px;height:522px;border-radius:42px;background:var(--panel)}
.title-brand{left:0;right:0;top:82px;justify-content:center;gap:18px}
.title-brand .brand__dot{width:58px;height:58px}
.title-brand .brand__name{font-size:48px}
.pill{left:318px;top:272px;width:443px;height:74px;border-radius:37px;background:var(--orange);color:var(--white);font-family:'Cinzel',serif;font-size:40px;text-align:center;line-height:76px}
.pill::after{content:"";position:absolute;left:207px;bottom:-14px;border-left:14px solid transparent;border-right:14px solid transparent;border-top:15px solid var(--orange)}
.kicker{left:0;right:0;top:380px;text-align:center;font-family:'Cinzel',serif;font-size:22px}
.topic{left:0;right:0;top:404px;text-align:center;font-size:34px}
.date{left:0;right:0;top:508px;display:flex;justify-content:center;align-items:center;gap:10px;font-family:'Cinzel',serif;font-size:20px}

/* slide 2 */
.side-panel{left:761px;top:0;width:292px;height:593px;background:var(--orange);border-radius:52px 0 0 52px}
.agenda{left:71px;top:182px;list-style:none}
.agenda li{display:flex;align-items:center;gap:14px;font-size:26px;font-weight:300;height:32.8px}

/* slide 3 */
.grey-panel{left:0;top:0;width:649px;height:593px;background:var(--panel);border-radius:0 40px 40px 0}
.lead{left:71px;top:230px;display:flex;align-items:center;gap:12px;font-size:28px;font-weight:500}
.lead-text{left:71px;top:302px;width:440px;font-size:26px;font-weight:300;line-height:32.5px}

/* slide 4 */
.slide--4{background:var(--white)}
.q-panel{left:0;top:0;width:1053px;height:497px;background:var(--panel-soft);border-radius:0 0 40px 40px}
.questions{left:352px;top:186px;width:650px;list-style:none}
.questions li{display:flex;gap:10px;font-size:18px;font-weight:300;line-height:24px;margin-bottom:24px}
.questions .tri{margin-top:5px;flex:none;border-top-width:6px;border-bottom-width:6px;border-left-width:8px}

/* slide 5 */
.pause{left:515px;top:241px;width:496px;height:73px;border-radius:37px;background:var(--white);font-family:'Cinzel',serif;font-size:40px;text-align:center;line-height:74px;color:var(--navy)}
.pause::after{content:"";position:absolute;left:48px;bottom:-14px;border-left:14px solid transparent;border-right:14px solid transparent;border-top:15px solid var(--white)}
.fun{left:566px;top:340px;font-family:'Cinzel',serif;font-size:26px;color:var(--white)}
</style>
</head>
<body>
<main class="canvas">

  <section class="slide slide--1">
    <div class="abs title-panel"></div>
    <div class="brand title-brand"><span class="brand__dot"></span><span class="brand__name">Jonas Wendelin</span></div>
    <div class="abs pill">Präsentation</div>
    <p class="abs kicker">Thematisch:</p>
    <p class="abs topic">Lorem ipsum dolor Dolore</p>
    <p class="abs date"><span class="tri"></span>Mittwoch, 6. Dezember 2023</p>
  </section>

  <section class="slide slide--2">
    <div class="abs side-panel"></div>
    <div class="bubble bubble--navy" style="top:32px;width:562px;height:74px;padding-top:22px"><p class="bubble__title">Agenda für die heutige Session</p></div>
    <ul class="abs agenda">
      <li><span class="tri"></span>Lorem ipsum dolor</li>
      <li><span class="tri"></span>Consectetuer adipiscing</li>
      <li><span class="tri"></span>Elitsed diam nonummy nibh</li>
      <li><span class="tri"></span>Dolore magna aliquam erat</li>
      <li><span class="tri"></span>Veniam, quis nostrud</li>
      <li><span class="tri"></span>Exerci tation ullamcorper</li>
      <li><span class="tri"></span>Suscipit lobortis nisl ut</li>
      <li><span class="tri"></span>Aliquip ex ea com</li>
    </ul>
    <svg class="art" style="left:485px;top:124px" width="518" height="382" role="img" aria-label="Illustration: zwei Personen sitzen im Gespräch auf einem Sofa, mit Sprechblasen und Wolken">
      <defs><linearGradient id="talkFill" x1="0" y1="0" x2="1" y2="1"><stop offset="0" stop-color="#7fd6de"/><stop offset="1" stop-color="#3f7f95"/></linearGradient></defs>
      <rect width="518" height="382" rx="24" fill="url(#talkFill)" opacity=".55"/>
    </svg>
    <div class="brand brand--corner brand--light"><span class="brand__dot" style="background:var(--white)"></span><span class="brand__name">Wendelin</span></div>
    <div class="brand brand--footer"><span class="brand__dot"></span><span class="brand__name">Jonas Wendelin</span></div>
    <div class="page-num page-num--on-orange">02</div>
  </section>

  <section class="slide slide--3">
    <div class="abs grey-panel"></div>
    <div class="bubble bubble--orange" style="top:33px;width:590px"><p class="bubble__title">Gemeinsamer Einstieg in den Tag</p><p class="bubble__sub">Check-In</p></div>
    <p class="abs lead"><span class="tri"></span>1 prägnanter Satz:</p>
    <p class="abs lead-text">Worauf freue ich mich heute am meisten, bzw. was interessiert mich besonders zu diesem Thema?</p>
    <svg class="art" style="left:704px;top:136px" width="319" height="376" role="img" aria-label="Illustration: springende Person mit erhobenen Armen vor Wolken und Sternen">
      <defs><linearGradient id="jumpFill" x1="0" y1="0" x2="0" y2="1"><stop offset="0" stop-color="#9fdfe5"/><stop offset="1" stop-color="#f68a52"/></linearGradient></defs>
      <rect width="319" height="376" rx="24" fill="url(#jumpFill)" opacity=".5"/>
    </svg>
    <div class="brand brand--corner"><span class="brand__dot"></span><span class="brand__name">Wendelin</span></div>
    <div class="brand brand--footer"><span class="brand__dot"></span><span class="brand__name">Jonas Wendelin</span></div>
    <div class="page-num">03</div>
  </section>

  <section class="slide slide--4">
    <div class="abs q-panel"></div>
    <div class="bubble bubble--navy" style="top:32px;width:590px"><p class="bubble__title">Meine Einstellungen zum Thema</p><p class="bubble__sub">Interviews</p></div>
    <svg class="art" style="left:47px;top:145px" width="264" height="326" role="img" aria-label="Illustration: nachdenkliche Person sitzt auf einem großen Fragezeichen">
      <defs><linearGradient id="thinkFill" x1="0" y1="0" x2="0" y2="1"><stop offset="0" stop-color="#6fd3dc"/><stop offset="1" stop-color="#d6d6d6"/></linearGradient></defs>
      <rect width="264" height="326" rx="24" fill="url(#thinkFill)" opacity=".6"/>
    </svg>
    <ul class="abs questions">
      <li><span class="tri"></span>Welche Erfahrungen hast du gemacht zum Thema öffentliche Wirksamkeit, Sicht- und Hörbarkeit?</li>
      <li><span class="tri"></span>Was glaubst du über dich selbst, in solchen Situationen?</li>
      <li><span class="tri"></span>Was denkst du, glauben die anderen über dich?</li>
      <li><span class="tri"></span>Was hast du diesbezüglich vorgelebt bekommen, von Modellen, Eltern, etc.?</li>
      <li><span class="tri"></span>Was gelingt dir leicht? Was schwer? Was möchtest du gerne verändern?</li>
    </ul>
    <div class="brand brand--corner"><span class="brand__dot"></span><span class="brand__name">Wendelin</span></div>
    <div class="brand brand--footer"><span class="brand__dot"></span><span class="brand__name">Jonas Wendelin</span></div>
    <div class="page-num">04</div>
  </section>

  <section class="slide slide--5">
    <svg class="art" style="left:41px;top:34px" width="455" height="462" role="img" aria-label="Illustration: Kaffeetasse von oben auf einer dunkleren Fläche">
      <defs><radialGradient id="cupFill" cx=".4" cy=".5" r=".6"><stop offset="0" stop-color="#f47a40"/><stop offset=".6" stop-color="#c9582f"/><stop offset="1" stop-color="#0b4a6c"/></radialGradient></defs>
      <rect width="455" height="462" rx="200" fill="url(#cupFill)" opacity=".75"/>
    </svg>
    <div class="abs pause">Eine kurze Pause...</div>
    <p class="abs fun">Viel Spass!</p>
    <div class="brand brand--corner brand--light"><span class="brand__dot"></span><span class="brand__name">Wendelin</span></div>
    <div class="brand brand--footer brand--light"><span class="brand__dot"></span><span class="brand__name">Jonas Wendelin</span></div>
    <div class="page-num page-num--light">05</div>
  </section>

</main>
</body>
</html>
```